Software company specialized in data analytics and professional services

We need a landing page design for our business. It should include our logo design. It should have multiple sections :
- stylish head
- what we do (data analytics software, professional services)
- contact form

Target Market(s)

Companies, B2B

Industry/Entity Type

Data

Number of Pages Required

1 page

Font styles to use
Sans Serif

Requirements
Must have
• Dark theme
Should not have
• Gradients on buttons

```html
<!DOCTYPE html>
<html lang="en">
<head>
<meta charset="utf-8">
<title>Tenfold – Data Analytics & Professional Services</title>
<link rel="stylesheet" href="https://fonts.googleapis.com/css2?family=Lora:wght@400;500;700&family=Open+Sans:wght@400;600;700&display=swap">
<style>
:root{
  --ink:#0b0b10;
  --magenta:#a3168f;
  --blue:#1f6ea6;
  --sky:#3aa3dc;
  --paper:#ffffff;
  --mist:#f1f1f3;
  --text:#4a4a52;
  --muted:#9a9aa4;
  --line:#d9d9de;
}
*{box-sizing:border-box;margin:0;padding:0}
html,body{width:1200px;height:4436px;overflow:hidden}
body{font-family:"Open Sans",sans-serif;color:var(--text);background:var(--paper);position:relative}
section,header,footer{position:absolute;left:0;width:1200px}
.btn{display:inline-block;background:var(--magenta);color:#fff;font:700 13px "Open Sans",sans-serif;letter-spacing:.5px;text-transform:uppercase;padding:12px 28px;border-radius:22px}
.para{font-size:13px;line-height:1.65;color:var(--text)}
.brand{font:700 26px "Open Sans",sans-serif;letter-spacing:1px;color:var(--magenta)}
.brand-dot{display:inline-block;width:12px;height:12px;border-radius:50%;background:var(--magenta);margin-right:8px;vertical-align:middle}
.section-title{font-family:"Lora",serif;font-weight:400;font-size:48px;color:var(--blue)}
.photo-area{position:absolute}

/* header */
.hero{top:0;height:560px;background:var(--ink);overflow:hidden}
.hero-photo{position:absolute;inset:0;background:radial-gradient(ellipse at 78% 55%,#6a2b7c 0%,#2b1a3b 32%,#111019 62%,#0b0b10 100%)}
.nav{position:absolute;top:20px;left:160px;width:880px;height:40px;display:flex;align-items:center}
.nav .brand{font-size:24px}
.nav-links{position:absolute;left:288px;display:flex;font-size:11px;font-weight:600;color:#fff;text-transform:uppercase}
.nav-links span{padding:0 16px}
.nav-links .active{border-bottom:2px solid var(--magenta);padding-bottom:4px}
.nav-call{position:absolute;left:740px;display:flex;align-items:center;gap:10px;color:#fff;font-size:11px;line-height:1.3}
.nav-call .ico{width:34px;height:34px;border-radius:50%;background:var(--blue);display:flex;align-items:center;justify-content:center}
.hero-copy{position:absolute;left:160px;top:218px;color:#fff}
.hero-copy .l1{font:400 44px "Lora",serif;letter-spacing:2px;line-height:1}
.hero-copy .l2{font:400 58px "Lora",serif;color:var(--sky);letter-spacing:2px;line-height:1.1}
.hero-copy .l3{font:400 22px "Lora",serif;letter-spacing:2.5px;margin-top:2px}
.hero-copy .btn{margin-top:26px}

/* about */
.about{top:560px;height:740px;background:var(--paper)}
.about-photo{left:150px;top:90px;width:420px;height:560px;background:linear-gradient(135deg,#8d9099,#4a4d57 55%,#b9bcc4)}
.about-copy{position:absolute;left:608px;top:110px;width:460px}
.about-copy .kicker{font:400 22px "Lora",serif;color:var(--ink)}
.about-copy h2{font:400 48px "Lora",serif;color:var(--blue);line-height:1.1;margin-bottom:24px}
.about-copy .para{margin-bottom:16px}
.about-copy .btn{margin-top:14px}

/* what we do */
.services{top:1300px;height:920px;background:radial-gradient(ellipse at 50% 60%,#1d1d26 0%,var(--ink) 70%)}
.services .section-title{position:absolute;top:86px;width:100%;text-align:center;color:#fff}
.services svg{position:absolute;left:0;top:0}
.service{position:absolute;width:160px;text-align:center;color:#c9c9d1;font-size:11px;line-height:1.5}
.service h3{font:600 14px "Open Sans",sans-serif;color:var(--magenta);margin-bottom:4px;white-space:nowrap}

/* experts */
.experts{top:2220px;height:580px;background:var(--mist)}
.experts-copy{position:absolute;left:160px;top:140px;width:500px}
.experts-copy .section-title{margin-bottom:22px}
.experts-copy .para{margin-bottom:16px}
.experts-photo{left:700px;top:70px;width:400px;height:440px;background:linear-gradient(135deg,#3b5d88,#1a2538 55%,#8aa1bf)}

/* news */
.news{top:2800px;height:720px;background:var(--paper)}
.news .section-title{position:absolute;top:82px;width:100%;text-align:center}
.news-card{position:absolute;overflow:hidden}
.news-photo{position:absolute;inset:0}
.news-card .date{position:absolute;left:40px;top:242px;background:var(--magenta);color:#fff;font-size:12px;font-weight:700;padding:8px 16px}
.news-card h3{position:absolute;font:400 22px "Lora",serif;color:#fff;line-height:1.3}
.news-card p{position:absolute;font-size:12px;color:#e5e5ea;line-height:1.5}
.news .btn{position:absolute;left:480px;top:608px}

/* contact */
.contact{top:3520px;height:560px;background:var(--mist)}
.contact .section-title{position:absolute;left:160px;top:118px}
.form{position:absolute;left:160px;top:212px;width:420px}
.form .row{display:flex;gap:14px;margin-bottom:14px}
.field{flex:1;height:40px;background:#fff;border:1px solid var(--line);font-size:11px;color:var(--muted);padding:12px 14px}
.field.area{height:74px}
.form .btn{margin-top:8px;border-radius:4px}
.contact-photo{left:640px;top:60px;width:420px;height:440px;background:linear-gradient(135deg,#2a4c80,#101b30 55%,#5f7ea8)}

/* footer */
.footer{top:4080px;height:320px;background:var(--ink);color:#c9c9d1}
.footer-col{position:absolute;top:62px}
.footer h4{font:700 15px "Open Sans",sans-serif;color:#fff;margin-bottom:14px}
.footer h4::after{content:"";display:block;width:26px;height:2px;background:var(--magenta);margin-top:6px}
.footer .para{color:#c9c9d1;font-size:12px}
.footer ul{list-style:none;font-size:12px;line-height:1.9}
.footer ul li::before{content:"› ";color:var(--magenta)}
.socials{display:flex;gap:8px;margin-top:16px}
.socials span{width:26px;height:26px;border-radius:50%;background:var(--blue)}
.subscribe-input{width:200px;height:30px;background:#fff;margin-bottom:10px}
.subscribe-btn{width:200px;height:30px;background:var(--magenta);color:#fff;font-size:12px;font-weight:700;text-align:center;line-height:30px;text-transform:uppercase}
.copyright{position:absolute;left:0;width:1200px;top:4400px;height:36px;background:#000;color:#9a9aa4;font-size:11px;text-align:center;line-height:36px}
</style>
</head>
<body>

<header class="hero">
  <div class="hero-photo" role="img" aria-label="Analyst working on a laptop with glowing data charts rising from the screen"></div>
  <nav class="nav">
    <div class="brand"><span class="brand-dot"></span>TENFOLD</div>
    <div class="nav-links">
      <span class="active">Home</span><span>About Us</span><span>What We Do</span><span>Our Experts</span><span>Contact Us</span>
    </div>
    <div class="nav-call">
      <div class="ico"><svg width="16" height="16" viewBox="0 0 24 24"><path fill="#fff" d="M6.6 10.8a15.1 15.1 0 0 0 6.6 6.6l2.2-2.2c.3-.3.7-.4 1-.2 1.1.4 2.3.6 3.6.6.6 0 1 .4 1 1V20c0 .6-.4 1-1 1A17 17 0 0 1 3 4c0-.6.4-1 1-1h3.5c.6 0 1 .4 1 1 0 1.3.2 2.5.6 3.6.1.3 0 .7-.2 1z"/></svg></div>
      <div>Call Us<br><strong>+1 (555) 010 2040</strong></div>
    </div>
  </nav>
  <div class="hero-copy">
    <div class="l1">DATA</div>
    <div class="l2">ANALYTICS</div>
    <div class="l3">PROFESSIONAL SERVICES</div>
    <span class="btn">Contact Us</span>
  </div>
</header>

<section class="about">
  <div class="photo-area about-photo" role="img" aria-label="Business team meeting in an office"></div>
  <div class="about-copy">
    <div class="kicker">About</div>
    <h2>Tenfold</h2>
    <p class="para">It is a long established fact that a reader will be distracted by the readable content of a page when looking at its layout. The point of using placeholder text is that it has a more-or-less normal distribution of letters, as opposed to using repeated content, making it look like readable English for publishing packages and web page editors that now use it as their default model text.</p>
    <p class="para">There are many variations of passages available, but the majority have suffered alteration in some form, by injected humour, or randomised words which don't look even slightly believable.</p>
    <span class="btn">Read More</span>
  </div>
</section>

<section class="services">
  <h2 class="section-title">What We Do</h2>
  <svg width="1200" height="920" viewBox="0 0 1200 920" aria-hidden="true">
    <path d="M352 400 Q600 700 848 400" fill="none" stroke="var(--magenta)" stroke-width="3"/>
    <circle cx="600" cy="320" r="158" fill="#2a2a33"/>
    <circle cx="600" cy="320" r="140" fill="#fff"/>
    <circle cx="600" cy="320" r="118" fill="none" stroke="#e4e4e8" stroke-width="2"/>
    <g fill="#e9e9ee" stroke="#fff" stroke-width="6">
      <circle cx="352" cy="400" r="34"/><circle cx="476" cy="512" r="34"/><circle cx="600" cy="550" r="34"/><circle cx="724" cy="512" r="34"/><circle cx="848" cy="400" r="34"/>
    </g>
    <g fill="var(--magenta)">
      <circle cx="388" cy="408" r="6"/><circle cx="812" cy="408" r="6"/><circle cx="600" cy="514" r="6"/><circle cx="506" cy="494" r="6"/><circle cx="694" cy="494" r="6"/>
    </g>
    <g fill="none" stroke="var(--blue)" stroke-width="2.5">
      <rect x="340" y="388" width="24" height="24" rx="3"/><path d="M346 406v-6M352 406v-10M358 406v-4"/>
      <circle cx="476" cy="512" r="11"/><path d="M476 505v7l5 3"/>
      <path d="M588 560h24M592 560v-12M600 560v-18M608 560v-8"/>
      <path d="M714 502h20v20h-20zM719 512h10"/>
      <path d="M836 412l8-10 6 6 10-14"/>
    </g>
    <text x="600" y="332" text-anchor="middle" font-family="Open Sans, sans-serif" font-weight="700" font-size="34" letter-spacing="1" fill="var(--magenta)">TENFOLD</text>
  </svg>
  <div class="service" style="left:272px;top:444px"><h3>Data Integrity</h3>It is a long established fact that a reader will be distracted by</div>
  <div class="service" style="left:768px;top:444px"><h3>Data Analytics</h3>It is a long established fact that a reader will be distracted by</div>
  <div class="service" style="left:396px;top:556px"><h3>Professional Services</h3>It is a long established fact that a reader will be distracted by</div>
  <div class="service" style="left:520px;top:614px"><h3>Data Consulting</h3>It is a long established fact that a reader will be distracted by</div>
  <div class="service" style="left:644px;top:556px"><h3>Data Reporting</h3>It is a long established fact that a reader will be distracted by</div>
</section>

<section class="experts">
  <div class="experts-copy">
    <h2 class="section-title">Our Experts</h2>
    <p class="para">It is a long established fact that a reader will be distracted by the readable content of a page when looking at its layout. The point of using placeholder text is that it has a more-or-less normal distribution of letters, making it look like readable English for many publishing packages and web page editors.</p>
    <p class="para">There are many variations of passages available, but the majority have suffered alteration in some form, by injected humour, or randomised words which don't look even slightly believable.</p>
    <span class="btn">Meet Our Expert</span>
  </div>
  <div class="photo-area experts-photo" role="img" aria-label="Analytics dashboards and charts on screens"></div>
</section>

<section class="news">
  <h2 class="section-title">Our Latest News</h2>
  <div class="news-card" style="left:160px;top:168px;width:528px;height:372px">
    <div class="news-photo" role="img" aria-label="Colleagues reviewing analytics on a laptop" style="background:linear-gradient(160deg,#9aa3b0,#4b5360 55%,#1c2029)"></div>
    <span class="date">06 DEC 2023</span>
    <h3 style="left:40px;top:290px;width:440px">Lorem Ipsum is simply dummy text</h3>
    <p style="left:40px;top:326px;width:440px">It is a long established fact that a reader will be distracted by the readable content.</p>
  </div>
  <div class="news-card" style="left:712px;top:168px;width:336px;height:176px">
    <div class="news-photo" role="img" aria-label="Team discussion around a meeting table" style="background:linear-gradient(160deg,#6e7480,#2a2f38)"></div>
    <h3 style="left:24px;top:100px;width:290px;font-size:18px">Lorem Ipsum is simply dummy text</h3>
  </div>
  <div class="news-card" style="left:712px;top:364px;width:336px;height:176px">
    <div class="news-photo" role="img" aria-label="Business people talking in a bright office" style="background:linear-gradient(160deg,#8b919c,#353a44)"></div>
    <h3 style="left:24px;top:100px;width:290px;font-size:18px">Lorem Ipsum is simply dummy text</h3>
  </div>
  <span class="btn">View Our Latest News</span>
</section>

<section class="contact">
  <h2 class="section-title">Contact Form</h2>
  <div class="form">
    <div class="row"><div class="field">First Name*</div><div class="field">Last Name*</div></div>
    <div class="row"><div class="field">Contact no*</div><div class="field">E-mail*</div></div>
    <div class="row"><div class="field area">Message</div></div>
    <span class="btn">Send Message</span>
  </div>
  <div class="photo-area contact-photo" role="img" aria-label="Hands working with data charts on a tablet"></div>
</section>

<footer class="footer">
  <div class="footer-col" style="left:160px;width:250px">
    <div class="brand" style="margin-bottom:14px"><span class="brand-dot"></span>TENFOLD</div>
    <p class="para">It is a long established fact that a reader will be distracted by the readable content of a page.</p>
    <div class="socials"><span></span><span></span><span></span><span></span></div>
  </div>
  <div class="footer-col" style="left:480px">
    <h4>Quick Links</h4>
    <ul><li>Home</li><li>About Us</li><li>What We Do</li><li>Our Experts</li><li>Contact Us</li></ul>
  </div>
  <div class="footer-col" style="left:644px;width:180px;font-size:12px;line-height:1.5">
    <h4>Contact</h4>
    <div>Phone:<br>+1 (555) 010 2040</div><br>
    <div>Email:<br>hello@tenfold-data.com</div><br>
    <div>Address:<br>48 Meridian Row, Lakeport</div>
  </div>
  <div class="footer-col" style="left:836px">
    <h4>Subscribe For Updates</h4>
    <div class="subscribe-input"></div>
    <div class="subscribe-btn">Subscribe</div>
  </div>
</footer>
<div class="copyright">Copyright 2023 Tenfold. All Rights Reserved.</div>

</body>
</html>
```